Stem Cell Injections

We are making a brochure for injecting stem cells into joints tendons and muscles to repair chronic and acute injuries.
i need a six page brochure
velumarq.com name of website
web sites that have similar feel are
http://www.tavicore.com/lumivaxx-procedures/
http://www.brindlova.com/stemcelltreatments/rheumatoidarthritisstemcelltreatment.html
http://www.brindlova.com/stemcellvideos/orthopedicstemcelltherapy.html
http://thewexholtclinic.com/bone-marrow-cell-concentrate-platelet-rich-plasma.asp
Requirements
Must have
- Graphics of injections into joints, tendons and muscle showing injections
for ideas please google image search "joint injections"
Nice to have
- we need personal bios of both doctors that do the procedures.
Should not have
- should look very modern not classic or old

```html
<!DOCTYPE html>
<html lang="en">
<head>
<meta charset="utf-8">
<title>PRP Therapy – Velumarq</title>
<link href="https://fonts.googleapis.com/css2?family=Cabin:wght@400;700&display=swap" rel="stylesheet">
<style>
  :root {
    --ink: #2d3a7c;
    --panel: #35437a;
    --paper: #ffffff;
    --photo-light: #f2f0ee;
    --photo-mid: #e4dcd6;
    --photo-skin: #d9b9a6;
  }
  html, body {
    margin: 0;
    padding: 0;
    overflow: hidden;
    background: var(--paper);
  }
  .page {
    position: relative;
    width: 928px;
    height: 1200px;
    overflow: hidden;
    background: var(--paper);
    font-family: "Cabin", "Gill Sans", sans-serif;
    color: var(--ink);
  }
  .hero-photo {
    position: absolute;
    left: 0;
    top: 0;
    width: 928px;
    height: 270px;
    background: linear-gradient(100deg, var(--photo-light) 0%, var(--photo-skin) 28%, var(--photo-mid) 45%, var(--photo-light) 62%, var(--photo-skin) 88%, var(--photo-mid) 100%);
  }
  .block {
    position: absolute;
    margin: 0;
  }
  .intro {
    left: 43px;
    top: 314px;
    width: 500px;
    font-weight: 700;
    font-size: 16.6px;
    line-height: 18.4px;
  }
  h2 {
    font-size: 19.6px;
    line-height: 19px;
    font-weight: 700;
    margin: 0;
  }
  h3 {
    font-size: 16.6px;
    line-height: 18.2px;
    font-weight: 700;
    margin: 0;
  }
  p {
    margin: 0;
    font-size: 16.3px;
    line-height: 18.2px;
  }
  .left { left: 43px; width: 500px; }
  .right { left: 583px; width: 270px; }
  .condition-list p strong { font-weight: 700; }
  .site-name { font-weight: 700; }
  .contact-panel {
    position: absolute;
    left: 583px;
    top: 970px;
    width: 268px;
    height: 230px;
    background: var(--panel);
    color: var(--paper);
    display: flex;
    justify-content: center;
    padding-top: 103px;
    box-sizing: border-box;
    font-size: 18px;
    letter-spacing: 0.2px;
  }
</style>
</head>
<body>
<div class="page">
  <div class="hero-photo" role="img" aria-label="Photo of a gloved hand holding a syringe, injecting into a patient's knee"></div>

  <p class="block intro">PRP therapy is a promising non-surgical treatment to accelerate the natural healing of osteoarthritis, tendons, ligaments and other soft tissue injuries without significant risk. As an emerging treatment, PRP uses the body's natural healing ability coupled with cutting edge science and technology to deliver fast healing and long-lasting results to soft-tissue injuries.</p>

  <section class="block left" style="top:462px">
    <h2>What is PRP therapy?</h2>
    <p>PRP, or platelet rich plasma, involves the use of a portion of a patient's own blood to encourage healing of injured ligaments, tendons, muscles and even joints. As the liquid portion of blood, plasma contains red and white blood cells, in addition to platelets. The high concentration of platelets acts as a catalyst to grow new soft tissue or bone cells. Essentially, PRP is protein that help repair and rejuvenate tendon and ligament fibers.</p>
  </section>

  <p class="block left" style="top:628px">Unlike cortisone shots, which sometimes are only a band-aid solution, PRP actually heals the injured area.</p>

  <section class="block left" style="top:702px">
    <h2>How is PRP therapy administered?</h2>
    <p>PRP therapy is administered through an injection. After extracting one or more tubes of a patient's blood, the blood is spun using a centrifuge machine to isolate the PRP with growth factors and separate red blood cells from platelets that release proteins. Next, after,topical and injected local anesthetic is applied, the activated platelets are injected in the injured tissues. Depending on the injury, ultrasound may be used to help guide the injection.</p>
  </section>

  <section class="block left condition-list" style="top:868px">
    <h2>What are some typical conditions treated<br>with PRP?</h2>
    <p><strong>Knee</strong> - Instability, partially strained or torn ligaments of the knee (MCL, ACL, or LCL), chondromalacia, meniscus tears, arthritis of the knee</p>
    <p><strong>Shoulder</strong> - Rotator cuff tear, rotator cuff tendinitis, bursitis, bicipital tendinitis, instability, labrum tear, arthritis of the shoulder</p>
    <p><strong>Hip</strong> - Bursitis, psoas tendinitis, Iliotibial band tendinitis (ITB Syndrome), sacroiliac joint dysfunction</p>
    <p><strong>Ankle</strong> - Ankle sprain, ankle tendinitis, achilles tendonitis, peroneal tendinitis, instability</p>
    <p><strong>Elbow / Hand / Wrist</strong> - Golfer's elbow, tennis elbow, trigger finger, finger tendonitis, arthritis of the elbow, hand, or wrist</p>
    <p><strong>Spine</strong> - Ligament sprain, rib conditions, whiplash injury, arthritis of the spine</p>
  </section>

  <section class="block right" style="top:316px">
    <h3>Are there any side effects to PRP therapy?</h3>
    <p>Because the therapy uses a patient's own blood, there are typically no negative side effects.</p>
    <p>Most patients tolerate PRP therapy quite well, although some patients report post-injection soreness. There is a risk of blood vessel or nerve injury when PRP is administered without the guidance of ultrasound.</p>
  </section>

  <section class="block right" style="top:552px">
    <h3>How long has PRP therapy been in use?</h3>
    <p>PRP was first used more than 20 years ago to improve wound healing in cancer patients and in maxillo-facial and jaw reconstruction plastic surgery. Its applications have since been extended to other fields of medicines, including cardiovascular surgery and orthopaedics. In the area of sports medicine, PRP has been used approximately 10 years. At <span class="site-name">Velumarq.com</span>, we compliment PRP therapy with the latest advanced techniques, like cytokine therapy, photomodulation, and supplements for cartilage and tendons to deliver the most beneficial results for our patients.</p>
  </section>

  <div class="contact-panel">www.Velumarq.com</div>
</div>
</body>
</html>
```